依頼詳細
●デザインの要望
・少し温かみ、やわらかさのあるデザイン(まるっこすぎない)
※参考例:poruくらいのやわらかさ
・そのほかの色については特に指定なし(現在の青は入れなくてOKです)
⇒カラフルにするかどうかもデザインの中で考えて頂いて結構です
・現在のアプリにある下記のボタンを全て実装する
※投稿ボタン、画面更新ボタン、履歴ボタン、オプションボタン、カテゴリ選択ボタン の5個
・投稿が表示されるマス目は正方形だけでなく長方形等もまぜてほしい
※現在は正方形オンリーですが、縦に2個くっつけたものや横に2個くっつけたものが入ってきたりするデザイン
⇒アプリ:Tiledeck の記事一覧画面のようなイメージ
・zelvonなのでzvos7のフラットなイメージ(がっつり立体的にはしてほしくないです)

●納品物
PSDファイル1個(zelvonで使用する倍のサイズの 1920x1280 くらいで作ってください)
可能であればレイヤーのあるPNGファイル(可能であればで結構です)

サイトURL
https://apps.trovenlo.jp/jp/app/id518203764?mt=8
ページ数
1ページ
希望イメージ
シンプル 複雑
単色 カラフル
暗い 明るい
日常 高級
遊び心 厳粛
未来的 伝統的
女性的 男性的
希望する色
小豆色や薄い茶色等温かみのある色全般
納品ファイル
• フォトショップ形式 (.psd)
• PNG形式 (.png)
補足説明
■ 選んだ理由

やわらかいテイストでかつ既存の青をさし色に入れて頂けたこと、
またプラスアルファとしてスプラッシュスクリーンをご提示いただけたため、
より実装後のアプリのイメージがわくことができました。

■ 提案者全員のお礼・コメント

たくさんのご提案ありがとうございました。
特にUIそのものまで提案して頂けたりと非常にこちらとしても勉強になる案件となりました。

上部のバーのデザインや、吹き出し型のデザイン、カラフル、マット等
かなり悩ませていただきました。
最終的にはより女性的で、かつ落ち着いている
という部分を基準に選ぶことにしました。

本アプリは今後もどんどん改良を加える予定のため、
また機会が有りましたら是非宜しくお願い致します。

```html
<!DOCTYPE html>
<html lang="ja">
<head>
<meta charset="utf-8">
<title>Tiledeck 記事一覧</title>
<link href="https://fonts.googleapis.com/css2?family=Noto+Sans+JP:wght@300;400;500&display=swap" rel="stylesheet">
<style>
:root{
  --page:#f3f1ee;
  --bar:#f7f6f4;
  --ink:#4a3b36;
  --paper:#ece8e1;
  --coral:#f07a78;
  --rose:#ee8a86;
  --mustard:#d9a54a;
  --cocoa:#5b3b33;
  --tan:#dfa57e;
  --peach:#e9b892;
  --banner-a:#c9c2b8;
  --banner-b:#e3ddd4;
  --line:#d8d2ca;
}
*{margin:0;padding:0;box-sizing:border-box}
html,body{width:800px;height:1200px;overflow:hidden;background:var(--page);font-family:"Noto Sans JP",sans-serif;color:var(--ink)}
.screen{position:absolute;left:62px;top:0;width:675px;height:1200px;background:var(--bar);overflow:hidden}
.status-bar{position:absolute;left:0;top:0;width:100%;height:45px;display:flex;align-items:center;justify-content:space-between;padding:0 16px;font-size:20px;font-weight:500;color:#222}
.status-bar .signal{display:flex;gap:4px}
.status-bar .signal span{width:9px;height:9px;border-radius:50%;background:#222}
.battery{width:40px;height:18px;border:2px solid #222;border-radius:3px;padding:2px}
.battery i{display:block;height:100%;width:80%;background:#222}
.banner{position:absolute;left:0;top:45px;width:100%;height:90px;background:linear-gradient(90deg,var(--banner-a),var(--banner-b) 60%,var(--banner-a))}
.tile-grid{position:absolute;left:0;top:135px;width:100%;height:945px;overflow:hidden}
.tile{position:absolute;overflow:hidden;padding:18px 22px;line-height:1.35}
.tile .headline{font-size:52px;font-weight:400;white-space:nowrap}
.tile .body{font-size:40px;font-weight:300;white-space:nowrap}
.tile .label{font-size:28px;font-weight:300;white-space:nowrap}
.tile .small{font-size:22px;font-weight:300;white-space:nowrap}
.paper{background:var(--paper);color:var(--ink)}
.coral{background:var(--coral);color:#fff}
.rose{background:var(--rose);color:#fff}
.mustard{background:var(--mustard);color:#fff}
.cocoa{background:var(--cocoa);color:#fff}
.tan{background:var(--tan);color:#fff}
.peach{background:var(--peach);color:#fff}
.toolbar{position:absolute;left:0;bottom:0;width:100%;height:112px;background:var(--bar);border-top:2px solid var(--line);display:flex;align-items:center;justify-content:space-around;padding:0 10px}
.toolbar svg{width:40px;height:40px;stroke:var(--ink);fill:none;stroke-width:3;stroke-linecap:round;stroke-linejoin:round}
.category{font-size:30px;font-weight:400;color:var(--ink)}
</style>
</head>
<body>
<main class="screen">
  <header class="status-bar">
    <div class="signal"><span></span><span></span><span></span><span></span><span></span></div>
    <div class="time">19:24</div>
    <div class="battery"><i></i></div>
  </header>
  <div class="banner" role="img" aria-label="広告バナーのイラスト"></div>

  <section class="tile-grid">
    <article class="tile mustard" style="left:-40px;top:0;width:135px;height:125px;padding-left:52px"><p class="label">さぽ</p><p class="small">いつも…</p></article>
    <article class="tile coral" style="left:-40px;top:135px;width:135px;height:225px"></article>
    <article class="tile paper" style="left:105px;top:0;width:365px;height:225px;padding:26px 24px"><p class="body">おります。</p><p class="body">早く!てかlumiere</p></article>
    <article class="tile rose" style="left:105px;top:235px;width:365px;height:125px"></article>
    <article class="tile coral" style="left:480px;top:0;width:195px;height:360px"><p class="label">スマホに</p></article>

    <article class="tile cocoa" style="left:-40px;top:370px;width:510px;height:220px;padding:26px 24px 0 64px"><p class="headline">スマホに変え</p><p class="small">いつも10分で使わなくなる</p><p class="small">休み中にちょっと</p></article>
    <article class="tile tan" style="left:480px;top:370px;width:195px;height:220px;padding:26px 20px"><p class="headline" style="font-size:36px">スマホに</p><p class="small">いつも10分で</p></article>

    <article class="tile peach" style="left:-40px;top:600px;width:135px;height:130px;padding-left:52px"><p class="label">さぽ</p></article>
    <article class="tile coral" style="left:-40px;top:740px;width:135px;height:160px"></article>
    <article class="tile tan" style="left:-40px;top:910px;width:135px;height:120px"></article>
    <article class="tile paper" style="left:105px;top:600px;width:470px;height:400px;padding:40px 28px"><p class="headline" style="font-size:60px">刻一刻と夏</p><p class="body">休みがちかづいて</p><p class="body">おります。</p><p class="body">早く!てかlumiere</p></article>
    <article class="tile rose" style="left:585px;top:600px;width:90px;height:160px"><p class="label">さ</p></article>
    <article class="tile coral" style="left:585px;top:770px;width:90px;height:310px"></article>
    <article class="tile tan" style="left:105px;top:1010px;width:470px;height:70px"></article>
  </section>

  <nav class="toolbar">
    <svg viewBox="0 0 40 40" aria-label="投稿"><path d="M8 32l4-10L28 6l6 6-16 16z"/><path d="M12 22l6 6"/></svg>
    <svg viewBox="0 0 40 40" aria-label="画面更新"><path d="M32 20a12 12 0 1 1-4-9"/><path d="M29 5v7h-7"/></svg>
    <svg viewBox="0 0 40 40" aria-label="履歴"><path d="M6 9h3M6 20h3M6 31h3M14 9h20M14 20h20M14 31h20"/></svg>
    <svg viewBox="0 0 40 40" aria-label="オプション"><circle cx="20" cy="20" r="7"/><path d="M20 3v5M20 32v5M3 20h5M32 20h5M8 8l4 4M28 28l4 4M8 32l4-4M28 12l4-4"/></svg>
    <span class="category">全体</span>
  </nav>
</main>
</body>
</html>
```